Stationary for Corwin Lattimore | ||
Business card, letterhead, with compliments slip, envelope | ||
Use same font as used in my logo | ||
Corporate Traditional Professional Simple |
[firstname] [surname] | ||
[title] | ||
1 Some Street Sometown Somewhereshire SW23 8SW |
someone@corwinlattimore.example | ||
www.corwinlattimore.example | ||
I am the sole employee at the moment. In the future, I hope to have other employees, so I will add a 'title' section later. Please bear this in mind when positioning the information. I am looking for something that is elegant, professional, minimilistic and tasteful. Please take a look at the website: http://www.corwinlattimore.example using the following credentials to log in: u/n: "pinewhisk" p/w: "pinewhisk847" Please feel free to message me for more information. Most importantly, I want the logo and other key information (like my name?) to be in silver (PMS 877 Metallic). |
I am flexible on this. I want space on my business cards for people to be able to write some information on. | ||

```html
<!DOCTYPE html>
<html lang="en">
<head>
<meta charset="utf-8">
<title>Corwin Lattimore — Stationery</title>
<link rel="stylesheet" href="https://fonts.googleapis.com/css2?family=Cormorant+Garamond:wght@400;500&family=Lato:wght@400&display=swap">
<style>
  :root {
    --silver: #97989a;
    --silver-light: #c9cacc;
    --silver-pale: #e4e5e6;
    --graphite: #6e6f71;
    --ink: #7c7d80;
    --paper: #ffffff;
    --edge: #d6d6d6;
    --backdrop: #ffffff;
  }
  * { box-sizing: border-box; margin: 0; padding: 0; }
  html, body { width: 1200px; height: 850px; overflow: hidden; background: var(--backdrop); }
  body { position: relative; font-family: "Lato", Arial, sans-serif; color: var(--ink); }

  .sheet { position: absolute; background: var(--paper); border: 1px solid var(--edge); overflow: hidden; }

  .wordmark { position: absolute; display: flex; align-items: center; gap: 7px;
    font-family: "Cormorant Garamond", Georgia, serif; font-weight: 500; color: var(--silver);
    text-transform: uppercase; line-height: 0.95; letter-spacing: 0.04em; }
  .wordmark .mark { width: 10px; height: 10px; background: var(--silver); flex: none; }
  .wordmark .name { border-left: 1px solid var(--silver); padding-left: 6px; }
  .wordmark.on-dark { color: #f1f1f1; }
  .wordmark.on-dark .mark { background: #f1f1f1; }
  .wordmark.on-dark .name { border-color: #f1f1f1; }

  .contact-strip { position: absolute; left: 0; right: 0; bottom: 0; }
  .contact-strip .line { font-size: 5.5px; letter-spacing: 0.08em; color: var(--ink);
    text-align: center; padding: 0 10px 4px; white-space: nowrap; }
  .contact-strip .band { height: 8px; background: var(--silver-light); }

  /* Letterhead */
  .letterhead { left: 29px; top: 24px; width: 547px; height: 792px; }
  .letterhead .wordmark { left: 34px; top: 28px; font-size: 19px; }
  .letterhead .statue { position: absolute; right: 22px; bottom: 40px; width: 100px; height: 175px;
    background: radial-gradient(ellipse at 50% 60%, var(--silver-pale), rgba(228,229,230,0.2) 70%, transparent 75%); }
  .letterhead .web { position: absolute; left: 0; right: 0; bottom: 36px; text-align: center;
    font-size: 7px; letter-spacing: 0.15em; color: var(--silver); }

  /* Envelope */
  .envelope { left: 593px; top: 24px; width: 583px; height: 252px; }
  .envelope svg { position: absolute; left: 0; top: 0; }
  .envelope .web { position: absolute; left: 0; right: 0; top: 18px; text-align: center;
    font-size: 7px; letter-spacing: 0.15em; color: #e8e8e8; }

  /* Compliments slip */
  .slip { left: 593px; top: 288px; width: 583px; height: 245px; }
  .slip .wordmark { left: 26px; top: 22px; font-size: 19px; }

  /* Business cards */
  .card { position: absolute; width: 244px; height: 133px; border: 1px solid var(--edge); overflow: hidden; }
  .card-front { top: 547px; display: flex; align-items: center; justify-content: center; }
  .card-front .wordmark { position: static; font-size: 17px; }
  .card-front.silver { left: 620px; background: linear-gradient(135deg, #f4f4f5 0%, #d7d8da 45%, #eeeff0 70%, #cfd0d2 100%); }
  .card-front.graphite { left: 890px; background: linear-gradient(135deg, #7a7b7d, #5f6062); }
  .card-front .web { position: absolute; bottom: 22px; left: 0; right: 0; text-align: center;
    font-size: 5px; letter-spacing: 0.15em; color: var(--graphite); }
  .card-front.graphite .web { color: #d8d8d8; }

  .card-back { top: 692px; background: var(--paper); padding: 14px 0 0 16px; }
  .card-back.left { left: 620px; }
  .card-back.right { left: 890px; }
  .card-back .person { font-family: "Cormorant Garamond", Georgia, serif; font-weight: 500;
    text-transform: uppercase; font-size: 11px; letter-spacing: 0.06em; color: var(--silver); }
  .card-back .role { font-size: 5px; letter-spacing: 0.12em; text-transform: uppercase; color: var(--ink); margin-top: 1px; }
  .card-back dl { margin-top: 13px; display: grid; grid-template-columns: 14px auto; row-gap: 3px;
    font-size: 5px; letter-spacing: 0.05em; color: var(--ink); }
  .card-back dt { color: var(--silver); }
  .card-back .statue { position: absolute; right: 8px; bottom: 4px; width: 70px; height: 95px;
    background: radial-gradient(ellipse at 50% 55%, var(--silver), rgba(151,152,154,0.35) 60%, transparent 72%); }
  .card-back .band { position: absolute; left: 0; right: 0; bottom: 0; height: 5px; background: var(--silver-light); }
</style>
</head>
<body>

  <!-- Letterhead -->
  <section class="sheet letterhead">
    <div class="wordmark"><span class="mark"></span><span class="name">Corwin<br>Lattimore</span></div>
    <div class="statue" role="img" aria-label="Faint silver classical statue figure"></div>
    <div class="web">www.corwinlattimore.example</div>
    <div class="contact-strip">
      <p class="line">1 Some Street, Sometown, Somewhereshire SW23 8SW &nbsp;|&nbsp; T: 01234 567890 &nbsp;|&nbsp; F: 01234 567891 &nbsp;|&nbsp; someone@corwinlattimore.example</p>
      <div class="band"></div>
    </div>
  </section>

  <!-- Envelope -->
  <section class="sheet envelope">
    <svg width="583" height="252" viewBox="0 0 583 252" aria-hidden="true">
      <path d="M0 0 H583 V84 Q583 104 555 106 Q291 122 28 106 Q0 104 0 84 Z" fill="#8e8f91"/>
    </svg>
    <div class="web">www.corwinlattimore.example</div>
  </section>

  <!-- Compliments slip -->
  <section class="sheet slip">
    <div class="wordmark"><span class="mark"></span><span class="name">Corwin<br>Lattimore</span></div>
    <div class="contact-strip">
      <p class="line">1 Some Street, Sometown, Somewhereshire SW23 8SW &nbsp;|&nbsp; T: 01234 567890 &nbsp;|&nbsp; F: 01234 567891 &nbsp;|&nbsp; someone@corwinlattimore.example</p>
      <div class="band"></div>
    </div>
  </section>

  <!-- Business card fronts -->
  <section class="card card-front silver">
    <div class="wordmark"><span class="mark"></span><span class="name">Corwin<br>Lattimore</span></div>
    <div class="web">www.corwinlattimore.example</div>
  </section>
  <section class="card card-front graphite">
    <div class="wordmark on-dark"><span class="mark"></span><span class="name">Corwin<br>Lattimore</span></div>
    <div class="web">www.corwinlattimore.example</div>
  </section>

  <!-- Business card backs -->
  <section class="card card-back left">
    <p class="person">Joe Bloggs</p>
    <p class="role">Director</p>
    <dl>
      <dt>T</dt><dd>01234 567890</dd>
      <dt>M</dt><dd>07700 900123</dd>
      <dt>E</dt><dd>someone@corwinlattimore.example</dd>
      <dt>W</dt><dd>www.corwinlattimore.example</dd>
    </dl>
    <div class="statue" role="img" aria-label="Silver classical statue figure"></div>
    <div class="band"></div>
  </section>
  <section class="card card-back right">
    <p class="person">Joe Bloggs</p>
    <p class="role">Director</p>
    <dl>
      <dt>T</dt><dd>01234 567890</dd>
      <dt>M</dt><dd>07700 900123</dd>
      <dt>E</dt><dd>someone@corwinlattimore.example</dd>
      <dt>W</dt><dd>www.corwinlattimore.example</dd>
    </dl>
    <div class="statue" role="img" aria-label="Silver classical statue figure"></div>
    <div class="band"></div>
  </section>

</body>
</html>
```